Marrow Cay Retreat Christmas wishes 2013

We require postcards designed to mail our to our clients for Christmas. We are a SURF travel company, with a high end market and like to mail our Christmas postcards to all our guests that have stayed with us through the year. Front cover will have images and text (ie Seasons Greeting) and our logo. The back will have space for TO: name & address and postage stamp. Will also have some basic text (ie The Management & Staff at Marrow Cay Retreat wish you and your family all the best for the Festive Season and New Year. We look forward to seeing you back at Marrow Cay Retreat again soon etc etc). Here is link to main image https://www.filecrate-demo.net/sh/qwmzrtpl83nvex/Rk7bPoQaZs

Target Market(s)

Our clients are mostly mature men (40-70) surfers who purchase luxury surf trips

Industry/Entity Type

Travel

Requirements
Must have
• Ocean Image (front)
Logo x 2 in same colour - Corvane & Marrow Cay Retreat (front)
Text (front)
Back to be white
Space for name & address (back)
Space for postage stamp (back)
Message (back)
Website www.corvanestays.net (back)

```html
<!DOCTYPE html>
<html lang="en">
<head>
<meta charset="utf-8">
<title>Marrow Cay Retreat – Season's Greetings Postcard</title>
<link rel="stylesheet" href="https://fonts.googleapis.com/css2?family=Kaushan+Script&family=Tinos:ital,wght@0,400;1,700&family=Arimo:wght@400;600&display=swap">
<style>
  :root {
    --stage: #101010;
    --paper: #ffffff;
    --ink: #111111;
    --rule: #9a9a9a;
    --frame: #ffffff;
    --sky-top: #2f6fc4;
    --sky-low: #8fb6e2;
    --sea-far: #1d5a9e;
    --sea-mid: #0e4f95;
    --sea-deep: #0a3f7c;
    --frost: #dde2f0;
    --badge: #0b0b0b;
  }
  * { box-sizing: border-box; margin: 0; padding: 0; }
  html, body { width: 1200px; height: 1186px; overflow: hidden; background: var(--stage); }
  .canvas { position: relative; width: 1200px; height: 1186px; }

  .postcard { position: absolute; left: 190px; width: 820px; height: 550px; overflow: hidden; }
  .postcard--front { top: 30px; }
  .postcard--back { top: 606px; background: var(--paper); }

  /* Front */
  .front-photo {
    position: absolute; inset: 0;
    background: linear-gradient(180deg, var(--sky-top) 0%, var(--sky-low) 24%, var(--sea-far) 27%, var(--sea-mid) 55%, var(--sea-deep) 100%);
  }
  .front-frame { position: absolute; inset: 20px; border: 4px solid var(--frame); }
  .front-title {
    position: absolute; left: 0; right: 0; top: 180px; text-align: center;
    font-family: "Kaushan Script", cursive; font-size: 76px; color: var(--paper);
    transform: rotate(-3deg);
  }
  .lodge-mark { position: absolute; top: 44px; right: 48px; text-align: right; color: var(--ink); font-family: "Arimo", sans-serif; }
  .lodge-mark__row { display: flex; align-items: center; justify-content: flex-end; gap: 6px; font-size: 12px; }
  .lodge-mark__dot { width: 12px; height: 12px; border: 1.5px solid var(--ink); border-radius: 50%; }
  .lodge-mark__region { font-size: 9px; margin-top: 1px; margin-right: 20px; }
  .group-badge {
    position: absolute; left: 66px; bottom: 62px; height: 26px; padding: 0 12px;
    display: flex; align-items: center; gap: 8px; background: var(--badge);
    color: var(--paper); font-family: "Arimo", sans-serif; font-size: 8px; letter-spacing: 1px;
  }
  .group-badge__square { width: 10px; height: 10px; background: var(--paper); }

  /* Back */
  .back-frost {
    position: absolute; left: 0; top: 0; width: 190px; height: 170px;
    background: radial-gradient(circle at 30% 30%, var(--frost) 0%, rgba(221,226,240,0.4) 45%, rgba(255,255,255,0) 70%);
  }
  .back-message {
    position: absolute; left: 40px; top: 150px; width: 360px; text-align: center;
    font-family: "Tinos", serif; font-size: 20px; line-height: 1.5; color: var(--ink);
  }
  .back-message__script { font-family: "Tinos", serif; font-style: italic; font-weight: 700; font-size: 26px; line-height: 1.2; display: block; }
  .back-divider { position: absolute; left: 440px; top: 60px; height: 400px; border-left: 1px solid var(--rule); }
  .stamp-box {
    position: absolute; right: 42px; top: 26px; width: 86px; height: 100px;
    border: 1.5px solid var(--rule); padding-top: 14px; text-align: center;
    font-family: "Arimo", sans-serif; font-size: 14px; line-height: 1.35; color: #777;
  }
  .address-lines { position: absolute; left: 490px; top: 250px; width: 280px; }
  .address-lines__line { border-top: 1px solid var(--rule); height: 56px; }
  .back-website { position: absolute; left: 40px; bottom: 34px; font-family: "Tinos", serif; font-size: 12px; color: var(--ink); }
</style>
</head>
<body>
<main class="canvas">
  <section class="postcard postcard--front">
    <div class="front-photo" role="img" aria-label="Ocean photograph: clear tropical blue water with a swimmer in the foreground and a surfer riding a distant wave under a cloud-dotted sky"></div>
    <div class="front-frame"></div>
    <div class="lodge-mark">
      <div class="lodge-mark__row"><span class="lodge-mark__dot"></span><span>marrowcayretreat.com</span></div>
      <div class="lodge-mark__region">indonesia</div>
    </div>
    <h1 class="front-title">Season’s Greetings</h1>
    <div class="group-badge"><span class="group-badge__square"></span><span>CORVANE LODGES &amp; RESORTS</span></div>
  </section>

  <section class="postcard postcard--back">
    <div class="back-frost" role="img" aria-label="Faint pale-blue snowflake decoration"></div>
    <p class="back-message">
      The Management &amp; Staff at<br>
      Marrow Cay Retreat joins in sending you<br>
      and your family
      <span class="back-message__script">Season’s Greeting</span>
      and Good Wishes for the upcoming
      <span class="back-message__script">New Year</span>
    </p>
    <div class="back-divider"></div>
    <div class="stamp-box">Place<br>Stamp<br>Here</div>
    <div class="address-lines">
      <div class="address-lines__line"></div>
      <div class="address-lines__line"></div>
      <div class="address-lines__line"></div>
    </div>
    <p class="back-website">www.corvanestays.net</p>
  </section>
</main>
</body>
</html>
```